Quorvix Letter head

Quorvix is a young and energetic software development consultancy. We spend our time working with clients to turn what ever is in their heads in to software.
We are trying to create an image of a high class software boutique who build class leading bespoke solutions.
We need a sharp letter head that looks great on high quality media.
We like bold colours and distinctive design. So show us what you can do.
Industry/Entity Type
Software
Requirements
Must have
- Our company is based in the UK and are requried to have on the paper somewhere the following information:
* Registered company name: Quorvix Ltd
* Registered company number
* VAT registration number
In addition we also want the following:
* An email address
* Telephone number
* Website address
An example of what some pages have in their footer is something like the following:
Quorvix Ltd is registered in England and Wales. Reg. no: 5316274
Registered office: 48 Cobblewick Road, Harlow Essex, CM93TP. Tel: 07712365081
You do not have to use this sentance but please make sure your design incorporates accommodates the requirements for UK based companies

```html
<!DOCTYPE html>
<html lang="en">
<head>
<meta charset="utf-8">
<title>Quorvix Letterhead</title>
<link rel="stylesheet" href="https://fonts.googleapis.com/css2?family=Arimo:wght@400;700&family=Saira:wght@400;500&display=swap">
<style>
  :root {
    --brand-red: #e21b26;
    --brand-red-dark: #b5121b;
    --band-grey: #8a8a8a;
    --band-grey-dark: #6f6f6f;
    --paper: #ffffff;
    --ink: #111111;
    --muted: #7a7a7a;
    --signature-blue: #2f7fc0;
  }
  * { margin: 0; padding: 0; box-sizing: border-box; }
  html, body { width: 902px; height: 1200px; overflow: hidden; background: var(--paper); }
  .letterhead { position: relative; width: 902px; height: 1200px; font-family: "Arimo", Arial, sans-serif; color: var(--ink); }
  .page-frame { position: absolute; inset: 0; }
  .brand-name {
    position: absolute; left: 39px; top: 40px;
    font-family: "Saira", sans-serif; font-weight: 500; font-size: 44px;
    letter-spacing: 1px; color: var(--brand-red); line-height: 1;
  }
  .website {
    position: absolute; right: 70px; top: 71px;
    font-family: "Saira", sans-serif; font-size: 12px; color: var(--muted);
  }
  .website strong { color: var(--brand-red); font-weight: 500; }
  .letter { position: absolute; left: 154px; top: 150px; width: 670px; font-size: 11px; line-height: 18.7px; }
  .letter-date { font-weight: 700; margin-bottom: 52px; }
  .letter-greeting { margin-bottom: 12px; }
  .letter p.body { margin-bottom: 18px; }
  .letter-closing { margin-top: 4px; }
  .signature {
    display: block; width: 104px; height: 50px; margin-top: 14px;
    background: linear-gradient(90deg, rgba(47,127,192,0.15), rgba(47,127,192,0.3));
    border-radius: 3px;
  }
  .sender-name { font-weight: 700; line-height: 13px; margin-top: 3px; }
  .sender-role { line-height: 13px; }
  .footer-contact {
    position: absolute; left: 157px; top: 1120px;
    font-family: "Saira", sans-serif; font-size: 10.5px; line-height: 13px; color: #fff;
  }
  .footer-company { padding-left: 14px; color: #ffd2d4; }
  .footer-line { display: flex; align-items: center; gap: 4px; }
  .footer-line svg { flex: none; }
  .footer-gap { display: inline-block; width: 12px; }
  .footer-registry {
    position: absolute; left: 155px; top: 1174px; display: flex; gap: 32px;
    font-family: "Saira", sans-serif; font-size: 10.5px; color: #fff;
  }
  .footer-registry span { display: flex; align-items: center; gap: 6px; }
  .dot { width: 8px; height: 8px; border-radius: 50%; background: #3a3a3a; display: inline-block; }
</style>
</head>
<body>
<div class="letterhead">
  <svg class="page-frame" width="902" height="1200" viewBox="0 0 902 1200" aria-hidden="true">
    <defs>
      <linearGradient id="greyBand" x1="0" y1="0" x2="0" y2="1">
        <stop offset="0" stop-color="#8a8a8a"/>
        <stop offset="1" stop-color="#6f6f6f"/>
      </linearGradient>
    </defs>
    <rect width="902" height="1200" fill="url(#greyBand)"/>
    <path d="M0 0 H871 V1124 A42 42 0 0 1 829 1166 H0 Z" fill="#e21b26"/>
    <path d="M862 0 H871 V1124 A42 42 0 0 1 829 1166 H0 V1160 H829 A33 33 0 0 0 862 1127 Z" fill="#b5121b"/>
    <path d="M0 0 H859 V1085 A28 28 0 0 1 831 1113 H0 Z" fill="#ffffff"/>
  </svg>

  <div class="brand-name">QUORVIX</div>
  <div class="website">www.<strong>Quorvix</strong>.com</div>

  <main class="letter">
    <p class="letter-date">Date: 28th October, 2013</p>
    <p class="letter-greeting">Dear Customer,</p>
    <p class="body">Lorem Ipsum is simply dummy text of the printing and typesetting industry. Lorem Ipsum has been the industry's Lorem Ipsum passages, and more recently with desktop publishing software like Inkwell Layout including standard dummy text ever since the 1500s, when an unknown printer took a galley of type and scrambled it to make a type specimen book. It has survived not only five centuries, but also the leap into electronic typesetting, remaining essentially unchanged. It was popularised in the 1960s with the release of Presstype sheets containing versions of Lorem Ipsum.</p>
    <p class="body">It is a long established fact that a reader will be distracted by the readable content of a page when looking at its layout. The point of using Lorem Ipsum is that it has a more-or-less normal distribution of letters, as opposed to using 'Content here, content here', making it look like readable English. Many desktop publishing packages and web page editors now use Lorem Ipsum as their default model text, and a search for 'lorem ipsum' will uncover many web sites still in their infancy. Various versions have evolved over the years, sometimes by accident, sometimes on purpose (injected humour and the like).</p>
    <p class="body">Contrary to popular belief, Lorem Ipsum is not simply random text. It has roots in a piece of classical Latin literature from 45 BC, making it over 2000 years old. Edwin Marlowe, a Latin professor at Ashgrove College in Virginia, looked up one of the more obscure Latin words, consectetur, from a Lorem Ipsum passage, and going through the cites of the word in classical literature, discovered the undoubtable source. Lorem Ipsum comes from sections 1.10.32 and 1.10.33 of "de Finibus Bonorum et Malorum" (The Extremes of Good and Evil) by Marcus Telvar, written in 45 BC. This book is a treatise on the theory of ethics, very popular during the Renaissance. The first line of Lorem Ipsum, "Lorem ipsum dolor sit amet..", comes from a line in section 1.10.32.</p>
    <p class="body">There are many variations of passages of Lorem Ipsum available, but the majority have suffered alteration in some form, by injected humour, or randomised words which don't look even slightly believable. If you are going to use a passage of Lorem Ipsum, you need to be sure there isn't anything embarrassing hidden in the middle of text. All the Lorem Ipsum generators on the Internet tend to repeat predefined chunks as necessary, making this the first true generator on the Internet. It uses a dictionary of over 200 Latin words, combined with a handful of model sentence structures, to generate Lorem Ipsum which looks reasonable. The generated Lorem Ipsum is therefore always free from repetition, injected humour, or non-characteristic words etc.</p>
    <p class="letter-closing">Regards,</p>
    <span class="signature" role="img" aria-label="Handwritten signature of the sender"></span>
    <p class="sender-name">SENDER NAME</p>
    <p class="sender-role">Designation</p>
  </main>

  <footer>
    <div class="footer-contact">
      <div class="footer-company">Quorvix Ltd.</div>
      <div class="footer-line">
        <svg width="9" height="11" viewBox="0 0 9 11" aria-hidden="true"><path d="M4.5 0A4 4 0 0 0 .5 4c0 3 4 7 4 7s4-4 4-7a4 4 0 0 0-4-4zm0 5.6A1.6 1.6 0 1 1 4.5 2.4a1.6 1.6 0 0 1 0 3.2z" fill="#5a0a0e"/></svg>
        <span>48 Cobblewick Road, Harlow Essex, CM93TP</span>
      </div>
      <div class="footer-line">
        <svg width="9" height="9" viewBox="0 0 9 9" aria-hidden="true"><circle cx="4.5" cy="4.5" r="4.5" fill="#5a0a0e"/></svg>
        <span>07712365081</span>
        <span class="footer-gap"></span>
        <svg width="12" height="8" viewBox="0 0 12 8" aria-hidden="true"><rect width="12" height="8" rx="1" fill="#5a0a0e"/><path d="M0.5 0.8 6 4.6 11.5 0.8" stroke="#e21b26" stroke-width="1" fill="none"/></svg>
        <span>customer.support@quorvix.com</span>
      </div>
    </div>
    <div class="footer-registry">
      <span><i class="dot"></i>5316274</span>
      <span><i class="dot"></i>GB 804217396</span>
    </div>
  </footer>
</div>
</body>
</html>
```